Product label for specialty fertilizer for cannabis

Create a label with our brand name and product information. The name of the new product is “Vardel” and the name is also the logo. The color palate is white/platinium/silver/shimmery. The product makes the flowers dense and hard so we want the logo to look strong and masculine. The liquid inside the bottle is white Which is what vardel means in Spanish
Also need a font for all the product information. See pics for example and
Target Market(s)
Cannabis growers
Industry/Entity Type
Cannabis
Colors
Designer to choose colors to be used in the design.
Requirements
Must have
- Strong visual presence for retail environment. Clean but bold look.
Nice to have
- Would be nice to have similar to a Tivo Mara font
Should not have
- Do not put any cannabis or marijuana images anywhere on the label

```html
<!DOCTYPE html>
<html lang="en">
<head>
<meta charset="utf-8">
<title>Vardel – Product Label</title>
<link rel="preconnect" href="https://fonts.googleapis.com">
<link rel="preconnect" href="https://fonts.gstatic.com" crossorigin>
<link href="https://fonts.googleapis.com/css2?family=Yesteryear&display=swap" rel="stylesheet">
<style>
  :root {
    --page-bg: #f1f2f4;
    --label-moss: #3c3d1f;
    --label-rust: #5a3516;
    --label-umber: #2a1a0c;
    --label-black: #050403;
    --brand-gold: #d9a31f;
  }
  * { margin: 0; padding: 0; box-sizing: border-box; }
  html, body {
    width: 1200px;
    height: 1200px;
    overflow: hidden;
    background: var(--page-bg);
  }
  .canvas {
    position: relative;
    width: 1200px;
    height: 1200px;
    display: flex;
    align-items: center;
    justify-content: center;
  }
  .label {
    position: relative;
    width: 800px;
    height: 1096px;
    overflow: hidden;
  }
  .label-texture {
    position: absolute;
    inset: 0;
    background:
      radial-gradient(ellipse 60% 40% at 30% 15%, rgba(70, 80, 30, 0.85), transparent 70%),
      radial-gradient(ellipse 55% 45% at 85% 45%, rgba(120, 60, 20, 0.75), transparent 70%),
      radial-gradient(ellipse 50% 35% at 15% 55%, rgba(95, 75, 45, 0.6), transparent 70%),
      linear-gradient(180deg, var(--label-moss) 0%, var(--label-rust) 45%, var(--label-umber) 72%, var(--label-black) 100%);
  }
  .brand-name {
    position: absolute;
    left: 40px;
    right: 40px;
    top: 310px;
    text-align: center;
    font-family: "Yesteryear", cursive;
    font-weight: 400;
    font-size: 270px;
    line-height: 1;
    color: var(--brand-gold);
    letter-spacing: -3px;
    white-space: nowrap;
  }
</style>
</head>
<body>
  <main class="canvas">
    <section class="label">
      <div class="label-texture" role="img" aria-label="Distressed grunge texture in moss green, rust brown and black"></div>
      <h1 class="brand-name">Vardel</h1>
    </section>
  </main>
</body>
</html>
```